Brackwell Immigration Law

We need a web design for our existing company www.brackwellcounsel.co.uk. We are an immigration consultancy. The final design should communicate professionalism, integrity and affordability.

Industry/Entity Type

It Company

Logo Text

Brackwell Counsel Partners

Number of Pages Required

5+ page

Font styles to use
Serif

Requirements
Must have
• I want to have the same silhouette logo but something different in positioning..
Nice to have
• Please have a look at these websites:
• https://www.travelpathguide.co.uk/visa_uk/
• http://www.oakdenadvisers.co.uk/
• http://www.myrtlegatelaw.org/index.php
• www.brackwellcounsel.co.uk

```html
<!DOCTYPE html>
<html lang="en">
<head>
<meta charset="utf-8">
<title>Brackwell Counsel Partners</title>
<link href="https://fonts.googleapis.com/css2?family=Open+Sans:wght@400;600;700&family=Raleway:wght@300;400;600;700&display=swap" rel="stylesheet">
<style>
:root{
  --accent:#1f9e8f;
  --accent-dark:#17786c;
  --ink:#333;
  --muted:#777;
  --light:#f3f5f5;
  --line:#e2e2e2;
  --footer:#232526;
  --footer-bar:#161717;
  --footer-text:#b9bdbd;
  --white:#fff;
}
*{box-sizing:border-box;margin:0;padding:0}
html,body{width:733px;height:1200px;overflow:hidden;background:var(--white)}
body{font-family:"Open Sans",Arial,sans-serif;color:var(--ink);font-size:8px;line-height:1.5}
.page{width:733px;height:1200px;position:relative}

/* header */
.site-header{height:48px;display:flex;justify-content:space-between;align-items:center;padding:0 45px;border-bottom:1px solid var(--line)}
.brand{display:flex;align-items:center;gap:6px}
.brand-mark{width:16px;height:16px;background:var(--accent)}
.brand-name{font-family:"Raleway",sans-serif;font-weight:600;font-size:10px;color:var(--ink)}
.header-right{text-align:right}
.call-line{font-size:8px;color:var(--muted);margin-bottom:4px}
.call-line strong{color:var(--ink);font-size:10px}
.main-nav{display:flex;gap:2px;justify-content:flex-end}
.main-nav a{font-size:7px;text-transform:uppercase;color:var(--ink);text-decoration:none;padding:3px 8px;font-weight:600}
.main-nav a.active{background:#2b2b2b;color:var(--white)}

/* hero */
.hero{position:relative;height:285px;overflow:hidden}
.hero-photo{position:absolute;inset:0;background:linear-gradient(100deg,#eef2f2 0%,#e4ebec 35%,#b9c6cc 60%,#56606a 85%,#2f363d 100%)}
.hero-copy{position:absolute;left:50px;top:70px;width:340px}
.hero-kicker{font-family:"Raleway",sans-serif;font-weight:300;font-size:17px;color:var(--accent-dark);letter-spacing:1px;white-space:nowrap}
.hero-title{font-family:"Raleway",sans-serif;font-weight:600;font-size:21px;color:var(--accent-dark);letter-spacing:.5px;margin-bottom:10px;white-space:nowrap}
.hero-text{font-size:8px;color:#555;margin-bottom:16px;width:270px}
.btn-outline{display:inline-block;border:1px solid #555;padding:5px 12px;font-size:7px;text-transform:uppercase;font-weight:600;color:#333;text-decoration:none}

/* sections */
.section{padding:0 45px}
.section-title{font-family:"Raleway",sans-serif;font-weight:700;font-size:11px;text-transform:uppercase;color:var(--ink);letter-spacing:.3px}
.section-sub{font-size:7.5px;color:var(--accent);margin-bottom:3px}
.section-rule{width:30px;height:2px;background:var(--accent);margin-bottom:10px}
.welcome{padding-top:22px;height:160px}
.welcome p{color:var(--muted);font-size:7.5px;margin-bottom:4px}

.news{height:285px;padding-top:6px}
.news-grid{display:flex;gap:22px}
.news-card{width:200px}
.news-photo{height:100px;background:linear-gradient(135deg,#c9d4dc,#8d9ba6);margin-bottom:8px}
.news-photo.b{background:linear-gradient(135deg,#e7d8c8,#b99d85)}
.news-photo.c{background:linear-gradient(135deg,#d9e3ea,#9cb0bf)}
.news-title{font-weight:700;font-size:8.5px;color:var(--ink)}
.news-meta{font-size:7px;color:var(--muted);margin-bottom:5px}
.news-text{font-size:7px;color:var(--muted);margin-bottom:4px}
.read-more{font-size:7px;color:var(--accent);text-decoration:none;font-weight:600}

.team{height:165px;padding-top:4px;border-top:1px solid var(--line)}
.team .section-title{margin-top:12px}
.team-grid{display:flex;justify-content:space-between;padding:0 30px}
.member{width:110px;text-align:center}
.member-photo{width:38px;height:38px;border-radius:50%;margin:0 auto 5px;background:linear-gradient(135deg,#d5dbe0,#7c8892)}
.member-name{font-weight:700;font-size:8px}
.member-text{font-size:6.5px;color:var(--muted)}

/* footer */
.site-footer{position:absolute;left:0;top:975px;width:733px;height:205px;background:var(--footer);padding:16px 45px 0;display:flex;gap:24px;color:var(--footer-text)}
.footer-col{width:143px}
.footer-col h4{font-size:7.5px;color:var(--white);text-transform:uppercase;margin-bottom:8px;font-weight:700}
.footer-col li{list-style:none;font-size:6.5px;text-transform:uppercase;padding:2px 0;border-bottom:1px solid #333}
.blog-item{display:flex;gap:6px;margin-bottom:8px}
.blog-thumb{width:30px;height:22px;flex:none;background:linear-gradient(135deg,#9aa8b3,#5d6a74)}
.blog-item p{font-size:6px;text-transform:uppercase;line-height:1.4}
.blog-item span{color:var(--accent);font-size:6px}
.contact-block p{font-size:6.5px;text-transform:uppercase;margin-bottom:5px}
.footer-bar{position:absolute;left:0;top:1180px;width:733px;height:20px;background:var(--footer-bar);color:var(--footer-text);font-size:6.5px;line-height:20px;padding:0 45px;text-transform:uppercase}
</style>
</head>
<body>
<div class="page">
  <header class="site-header">
    <div class="brand"><span class="brand-mark"></span><span class="brand-name">Brackwell Counsel Partners</span></div>
    <div class="header-right">
      <div class="call-line">Call us for consultation: <strong>0208 555 0142</strong></div>
      <nav class="main-nav">
        <a class="active" href="#">Home</a><a href="#">About us</a><a href="#">Join us</a><a href="#">Contact us</a><a href="#">Blog</a>
      </nav>
    </div>
  </header>

  <section class="hero">
    <div class="hero-photo" role="img" aria-label="Business professionals shaking hands in an office setting"></div>
    <div class="hero-copy">
      <div class="hero-kicker">LOREM IPSUM DOLOR</div>
      <div class="hero-title">CONSEC TETUR ADIPISICIN</div>
      <p class="hero-text">Lorem ipsum dolor sit amet, consectetur adipiscing elit, sed do eiusmod tempor incididunt ut labore et dolore magna aliqua. Ut enim ad minim.</p>
      <a class="btn-outline" href="#">Learn more</a>
    </div>
  </section>

  <section class="section welcome">
    <h2 class="section-title">Welcome to Brackwell Counsel Partners</h2>
    <div class="section-sub">Specialised in all sorts of immigration matters</div>
    <div class="section-rule"></div>
    <p>Brackwell Counsel Partners is regulated by the Migration Advice Standards Board (MASB) and we have built our reputation on good quality legal work which results in a high percentage of positive outcomes.</p>
    <p>The majority of our clients come from personal recommendations as we are known for our up-to-date legal knowledge, attention to detail and exceptional client care.</p>
    <p>We are proud to be members of the Association of Migration Advisers (AMA) and the Council for Migrant Support (CMS) in the United Kingdom.</p>
  </section>

  <section class="section news">
    <h2 class="section-title">News &amp; Publications</h2>
    <div class="section-sub">Specialised in all sorts of immigration matters</div>
    <div class="section-rule"></div>
    <div class="news-grid">
      <article class="news-card">
        <div class="news-photo" role="img" aria-label="Colleagues in a business meeting"></div>
        <div class="news-title">Duis aute irure dolor in reprehenderit in</div>
        <div class="news-meta">Posted by Helen Marsh</div>
        <p class="news-text">Neque porro quisquam est, qui dolorem ipsum quia dolor sit amet, consectetur, adipisci velit, sed quia non numquam eius modi tempora.</p>
        <a class="read-more" href="#">Read More</a>
      </article>
      <article class="news-card">
        <div class="news-photo b" role="img" aria-label="Smiling family portrait"></div>
        <div class="news-title">Duis aute irure dolor in reprehenderit in</div>
        <div class="news-meta">Posted by Helen Marsh</div>
        <p class="news-text">Neque porro quisquam est, qui dolorem ipsum quia dolor sit amet, consectetur, adipisci velit, sed quia non numquam eius modi tempora.</p>
        <a class="read-more" href="#">Read More</a>
      </article>
      <article class="news-card">
        <div class="news-photo c" role="img" aria-label="Graduate student holding a diploma"></div>
        <div class="news-title">Duis aute irure dolor in reprehenderit in</div>
        <div class="news-meta">Posted by Helen Marsh</div>
        <p class="news-text">Neque porro quisquam est, qui dolorem ipsum quia dolor sit amet, consectetur, adipisci velit, sed quia non numquam eius modi tempora.</p>
        <a class="read-more" href="#">Read More</a>
      </article>
    </div>
  </section>

  <section class="section team">
    <h2 class="section-title">Our Team</h2>
    <div class="section-sub">Specialised in all sorts of immigration matters</div>
    <div class="section-rule"></div>
    <div class="team-grid">
      <div class="member"><div class="member-photo" role="img" aria-label="Team member portrait"></div><div class="member-name">Daniel Rowe</div><p class="member-text">Senior adviser on visas and family settlement cases</p><a class="read-more" href="#">Read More</a></div>
      <div class="member"><div class="member-photo" role="img" aria-label="Team member portrait"></div><div class="member-name">Daniel Rowe</div><p class="member-text">Senior adviser on visas and family settlement cases</p><a class="read-more" href="#">Read More</a></div>
      <div class="member"><div class="member-photo" role="img" aria-label="Team member portrait"></div><div class="member-name">Daniel Rowe</div><p class="member-text">Senior adviser on visas and family settlement cases</p><a class="read-more" href="#">Read More</a></div>
      <div class="member"><div class="member-photo" role="img" aria-label="Team member portrait"></div><div class="member-name">Daniel Rowe</div><p class="member-text">Senior adviser on visas and family settlement cases</p><a class="read-more" href="#">Read More</a></div>
    </div>
  </section>

  <footer class="site-footer">
    <div class="footer-col">
      <h4>Quick links</h4>
      <ul><li>Home</li><li>About us</li><li>Join us</li><li>Contact us</li><li>Blog</li></ul>
    </div>
    <div class="footer-col">
      <h4>Immigration law</h4>
      <ul><li>Entry clearance (immigrant visa)</li><li>Immigration appeals</li><li>Settlement applications</li><li>Domestic workers visa</li><li>Student visa</li><li>Overstayers</li><li>Naturalisation</li><li>Immigration detention</li></ul>
    </div>
    <div class="footer-col">
      <h4>Recent from blog</h4>
      <div class="blog-item"><div class="blog-thumb" role="img" aria-label="Blog post thumbnail"></div><div><p>Guide to permanent residency in the UK</p><span>July 17, 2016</span></div></div>
      <div class="blog-item"><div class="blog-thumb" role="img" aria-label="Blog post thumbnail"></div><div><p>New rules for student visa holders</p><span>July 17, 2016</span></div></div>
    </div>
    <div class="footer-col contact-block">
      <h4>Contact us</h4>
      <p>London office</p>
      <p>Brackwell Counsel Partners<br>14 Carrow Lane<br>London EC2A 4RT</p>
      <p>London area</p>
      <p>Tel: 0208 555 0142<br>info@brackwellcounsel.co.uk</p>
    </div>
  </footer>
  <div class="footer-bar">© 2016. By Brackwell Counsel Partners</div>
</div>
</body>
</html>
```